Electrical Contracting Business Website

Require website done for my contracting business.
Partly done one but really dont have time.

You can view the current one at http://brelton.net.au

You can use any info/styles/photos from the current website

I like the orange color of the logo so id like things to be with that
Unfortunatly being a new business (Sept 2015) I havent got alot of photos . but if you require any for any of the specifics listed in the doc file ill have a look to see what I have.

I am targeting mainly commercial / industrial clients. Which also includes government and mining.

Target Market(s)

People requiring electricians

Industry/Entity Type

Electrician

Coding

Number of Pages Required

Colors
f37122

Requirements
Must have
• logo with EC Number
• Keep it simple and not to complicated
• Comply with the current html / style sheet standards.
• Desktop/Mobile Version compatability
Nice to have
• additional photos.
• The domestic lifts we install are by vostrel I dont have any photos of them unfortunately.
Should not have
• change colour of logo

```html
<!DOCTYPE html>
<html lang="en">
<head>
<meta charset="utf-8">
<title>Brelton Engineering – Specialized Electrical Services</title>
<link href="https://fonts.googleapis.com/css2?family=Raleway:wght@500;600;700;800&family=Open+Sans:wght@400;600;700&display=swap" rel="stylesheet">
<style>
:root{
  --orange:#f37122;
  --orange-deep:#ec5a24;
  --ink:#222;
  --text:#555;
  --muted:#888;
  --line:#e2e2e2;
  --dark:#1d1f26;
  --footer:#2b2b2b;
  --white:#fff;
}
*{box-sizing:border-box;margin:0;padding:0}
html,body{width:1200px;height:2597px;overflow:hidden}
body{position:relative;background:var(--white);font-family:"Open Sans",Arial,sans-serif;color:var(--text)}
.abs{position:absolute}

/* hero */
.hero{left:0;top:0;width:1200px;height:741px;
  background:linear-gradient(180deg,#2b2f38 0%,#3a3a3e 30%,#6b4a34 58%,#c0702c 70%,#3b2a22 76%,#1e2026 88%,#2b3038 100%)}
.hero-title{left:0;top:348px;width:1200px;text-align:center;font-family:"Raleway",sans-serif;font-weight:800;font-size:48px;line-height:56px;letter-spacing:3px;color:var(--white)}
.btn{left:537px;top:492px;width:126px;height:40px;background:var(--orange-deep);color:var(--white);font-family:"Open Sans",sans-serif;font-size:16px;line-height:40px;text-align:center}

/* header */
.header{left:47px;top:26px;width:1106px;height:118px;background:var(--white);border-bottom:5px solid var(--orange-deep)}
.brand{left:0;top:0;width:265px;height:113px;display:flex;align-items:center;justify-content:center;gap:10px;border-right:1px solid var(--line)}
.brand-mark{width:22px;height:22px;border-radius:50%;background:var(--orange-deep)}
.brand-name{font-family:"Raleway",sans-serif;font-weight:800;font-size:30px;color:var(--orange-deep)}
.brand-ec{position:absolute;left:0;bottom:14px;width:265px;text-align:center;font-size:9px;color:var(--orange-deep)}
.topbar{left:265px;top:0;width:841px;height:48px;border-bottom:1px solid var(--line);display:flex;font-size:12px;color:var(--muted)}
.topbar .cell{height:48px;display:flex;align-items:center;gap:7px;padding:0 19px;border-right:1px solid var(--line)}
.topbar .cell svg{width:12px;height:12px;fill:var(--muted)}
.socials{margin-left:auto;display:flex}
.socials span{width:44px;height:48px;border-left:1px solid var(--line);display:flex;align-items:center;justify-content:center}
.socials span i{width:10px;height:10px;background:#9a9a9a;display:block}
.nav{right:20px;top:48px;height:65px;display:flex;align-items:center;gap:42px;font-family:"Raleway",sans-serif;font-weight:500;font-size:15px;color:#333;letter-spacing:.3px}

/* section headings */
.sec-title{left:0;width:1200px;text-align:center;font-family:"Raleway",sans-serif;font-weight:600;font-size:32px;letter-spacing:1.5px;color:var(--ink)}
.sec-rule{left:546px;width:108px;height:2px;background:#999}

/* service cards */
.card{top:880px;width:341px;height:362px;border:1px solid var(--line);background:var(--white);text-align:center}
.card-photo{position:relative;height:242px}
.card-photo svg{position:absolute;left:0;bottom:0;width:100%;height:40px}
.card-name{margin-top:6px;font-family:"Raleway",sans-serif;font-weight:600;font-size:19px;letter-spacing:1px;color:var(--ink)}
.card-text{margin:8px auto 0;width:260px;font-size:11px;line-height:19px;color:var(--muted)}
.card-more{display:inline-block;margin-top:10px;font-family:"Raleway",sans-serif;font-weight:700;font-size:12px;color:var(--orange-deep);border-bottom:2px solid var(--orange-deep);padding-bottom:2px}

/* services include band */
.band{left:0;top:1313px;width:1200px;height:436px;background:linear-gradient(100deg,#1e1f22 0%,#2d2f33 45%,#3a3c40 100%)}
.band-photo{left:537px;top:1313px;width:663px;height:436px;clip-path:polygon(208px 0,663px 0,663px 436px,0 436px);
  background:linear-gradient(160deg,#6f6c68 0%,#8a7a5e 35%,#c9a77e 55%,#5d6470 80%,#3b4049 100%)}
.band-title{left:50px;top:1355px;font-family:"Raleway",sans-serif;font-weight:700;font-size:34px;color:var(--orange-deep);letter-spacing:.5px}
.list{list-style:none;font-size:19px;color:var(--white)}
.list li{height:37px;display:flex;align-items:center;gap:14px}
.list li::before{content:"";width:7px;height:7px;background:var(--orange-deep);transform:rotate(45deg)}
.list.col1{left:54px;top:1417px}
.list.col2{left:323px;top:1413px}

/* testimonials */
.bubble{font-size:15px;line-height:26px;color:var(--white)}
.bubble-orange{left:74px;top:1900px;width:527px;height:182px;background:var(--orange-deep);padding:28px 30px 0 26px}
.bubble-dark{left:601px;top:1923px;width:527px;height:135px;background:var(--dark);padding:44px 30px 0 46px;font-size:14px}
.tail{width:0;height:0;border-style:solid}
.tail-orange{left:206px;top:2082px;border-width:20px 14px 0 14px;border-color:var(--orange-deep) transparent transparent transparent}
.tail-dark{left:972px;top:2058px;border-width:18px 12px 0 12px;border-color:var(--dark) transparent transparent transparent}
.avatar{width:104px;height:104px;border-radius:50%;border:4px solid #f1f1f1}
.avatar-a{left:170px;top:2122px;background:radial-gradient(circle at 50% 40%,#e9c9a8,#b9835c 60%,#e8e2da)}
.avatar-b{left:949px;top:2104px;background:radial-gradient(circle at 50% 40%,#e6c3a4,#6b4a3a 60%,#d9dde2)}
.person-name{font-family:"Raleway",sans-serif;font-weight:600;font-size:17px;color:var(--ink);letter-spacing:.5px}
.person-role{font-size:13px;color:var(--text);margin-top:4px}
.person-a{left:288px;top:2138px}
.person-b{right:270px;top:2116px;text-align:right}

/* footer */
.footer{left:0;top:2276px;width:1200px;height:275px;background:var(--footer);color:#ddd}
.f-col{top:2312px}
.f-head{font-family:"Raleway",sans-serif;font-weight:500;font-size:17px;color:var(--white);padding-bottom:12px;border-bottom:1px solid #666}
.f-links{list-style:none;margin-top:14px;font-size:13px}
.f-links li{height:28px;display:flex;align-items:center;gap:10px}
.f-links li::before{content:"›";font-size:15px}
.f-text{margin-top:16px;font-size:13px;line-height:22px}
.f-text b{font-weight:700}
.f-contact{display:flex;align-items:center;gap:10px;font-size:13px;line-height:22px}
.f-contact svg{width:13px;height:13px;fill:#ddd}
.f-input{width:226px;height:38px;background:#f5f5f5;margin-top:16px}
.f-submit{margin:16px 0 0 155px;width:72px;height:34px;background:#000;color:var(--white);font-size:13px;line-height:34px;text-align:center}
.badge{left:960px;top:2332px;width:162px;height:74px;background:#5b5b5b}
.diamonds{left:946px;top:2448px;display:flex;gap:15px}
.diamonds span{width:30px;height:30px;background:#000;transform:rotate(45deg)}
.diamonds span:nth-child(3){background:#3a3a3a}
.copy{left:0;top:2551px;width:1200px;height:46px;background:var(--orange-deep);color:var(--white);font-size:13px;display:flex;align-items:center;justify-content:space-between;padding:0 55px 0 55px}
</style>
</head>
<body>

<div class="abs hero" role="img" aria-label="Harbour cranes silhouetted against a sunset sky over water"></div>

<header class="abs header">
  <div class="abs brand">
    <span class="brand-mark"></span><span class="brand-name">Brelton</span>
    <span class="brand-ec">Electrical Contractor EC 40317</span>
  </div>
  <div class="abs topbar">
    <div class="cell"><svg viewBox="0 0 24 24"><path d="M6.6 10.8a15 15 0 0 0 6.6 6.6l2.2-2.2c.3-.3.7-.4 1-.2 1.1.4 2.3.6 3.6.6.6 0 1 .4 1 1V20c0 .6-.4 1-1 1A17 17 0 0 1 3 4c0-.6.4-1 1-1h3.5c.6 0 1 .4 1 1 0 1.3.2 2.5.6 3.6.1.3 0 .7-.2 1z"/></svg>+124 45 90 312</div>
    <div class="cell" style="color:var(--orange-deep)"><svg viewBox="0 0 24 24"><path d="M2 5h20v14H2zm2 2v.5l8 5 8-5V7zm0 2.8V17h16V9.8l-8 5z"/></svg>support@brelton.net.au</div>
    <div class="cell"><svg viewBox="0 0 24 24"><path d="M12 2a10 10 0 1 0 0 20 10 10 0 0 0 0-20zm0 2a8 8 0 1 1 0 16 8 8 0 0 1 0-16zm-1 3v6l5 3 1-1.6-4-2.4V7z"/></svg>Mon - Fri : 08.00 - 17.00</div>
    <div class="socials"><span><i></i></span><span><i></i></span><span><i></i></span><span><i></i></span></div>
  </div>
  <nav class="abs nav"><span>ABOUT US</span><span>RESIDENTIAL</span><span>COMMERICAL</span><span>INDUSTRIAL</span><span>CONTACT US</span></nav>
</header>

<h1 class="abs hero-title">SPECIALIZED ELECTRICAL<br>SERVICES</h1>
<div class="abs btn">Read More</div>

<h2 class="abs sec-title" style="top:784px">OUR SERVICES</h2>
<div class="abs sec-rule" style="top:843px"></div>

<article class="abs card" style="left:59px">
  <div class="card-photo" role="img" aria-label="Residential switchboard with circuit breakers" style="background:linear-gradient(135deg,#c9cdd2,#e8e9ea 45%,#8d9399)">
    <svg viewBox="0 0 341 40" preserveAspectRatio="none"><polygon points="0,40 0,30 170,2 341,30 341,40" fill="var(--orange-deep)"/><polygon points="0,40 0,40 170,14 341,40" fill="#fff"/></svg>
  </div>
  <h3 class="card-name">RESIDENTIAL</h3>
  <p class="card-text">Claritas est etiam processus dynamicus, qui sequitur mutationem.</p>
  <span class="card-more">READ MORE</span>
</article>

<article class="abs card" style="left:430px">
  <div class="card-photo" role="img" aria-label="Commercial electric motor close-up" style="background:linear-gradient(135deg,#4a4a4a,#8b8b87 45%,#d8d6cf)">
    <svg viewBox="0 0 341 40" preserveAspectRatio="none"><polygon points="0,40 0,30 170,2 341,30 341,40" fill="#fff"/></svg>
  </div>
  <h3 class="card-name">COMMERICAL</h3>
  <p class="card-text">Claritas est etiam processus dynamicus, qui sequitur mutationem.</p>
  <span class="card-more" style="border:0">READ MORE</span>
</article>

<article class="abs card" style="left:798px">
  <div class="card-photo" role="img" aria-label="Industrial panel with rows of labelled breakers" style="background:linear-gradient(180deg,#1c1c1c,#3d3a2e 45%,#b3ad94 70%,#6a6a6a)">
    <svg viewBox="0 0 341 40" preserveAspectRatio="none"><polygon points="0,40 0,30 170,2 341,30 341,40" fill="#fff"/></svg>
  </div>
  <h3 class="card-name">INDUSTRIAL</h3>
  <p class="card-text">Claritas est etiam processus dynamicus, qui sequitur mutationem.</p>
  <span class="card-more" style="border:0">READ MORE</span>
</article>

<section>
  <div class="abs band" role="img" aria-label="Dimmed background of electrical wiring work"></div>
  <div class="abs band-photo" role="img" aria-label="Smiling electrician in a yellow hard hat at a switchboard"></div>
  <h2 class="abs band-title">Our Services Include:</h2>
  <ul class="abs list col1">
    <li>Electrical Installations</li><li>Voice, and Data Cabling</li><li>Electrical Modifications</li><li>Fault Finding</li><li>Panel Upgrades</li><li>Security Lighting</li>
  </ul>
  <ul class="abs list col2">
    <li>Generator Hookup</li><li>Surge Protection</li><li>Building Maintenance</li><li>Lift Maintenance</li><li>Crane/Hoist Maintenance</li><li>Labour Hire</li>
  </ul>
</section>

<h2 class="abs sec-title" style="top:1798px">OUR TESTIMONIALS</h2>
<div class="abs sec-rule" style="top:1857px"></div>

<blockquote class="abs bubble bubble-orange">Lorem ipsum dolor sit amet, consectetur adipisicing elit, sed do eiusmod tempor incididunt ut labore et dolore magna aliqua. Ut enim ad minim veniam, quis nostrud exercitation ullamco laboris nisi ut aliquip ex ea commodo consequat. Duis aute irure dolor.</blockquote>
<div class="abs tail tail-orange"></div>
<blockquote class="abs bubble bubble-dark">These guys solved my problem in a moment. Highly recommended!</blockquote>
<div class="abs tail tail-dark"></div>

<div class="abs avatar avatar-a" role="img" aria-label="Portrait photo of client"></div>
<div class="abs person-a"><div class="person-name">Jane Doe</div><div class="person-role">Enginer of Media Production</div></div>
<div class="abs avatar avatar-b" role="img" aria-label="Portrait photo of client"></div>
<div class="abs person-b"><div class="person-name">Jane Doe</div><div class="person-role">Enginer of Media Production</div></div>

<footer>
  <div class="abs footer"></div>
  <div class="abs f-col" style="left:80px;width:192px">
    <div class="f-head">Quick Link</div>
    <ul class="f-links"><li>About Us</li><li>Residential</li><li>Commerical</li><li>Industrial</li><li>Contact Us</li></ul>
  </div>
  <div class="abs f-col" style="left:333px;width:216px">
    <div class="f-head">Send Your Enquiry</div>
    <p class="f-text"><b>Brelton Engineering Pty Ltd</b><br>Call us any time or visit:<br>Carrow Vale, Western<br>Australia, 6099.</p>
    <div class="f-contact" style="margin-top:16px"><svg viewBox="0 0 24 24"><path d="M6.6 10.8a15 15 0 0 0 6.6 6.6l2.2-2.2c.3-.3.7-.4 1-.2 1.1.4 2.3.6 3.6.6.6 0 1 .4 1 1V20c0 .6-.4 1-1 1A17 17 0 0 1 3 4c0-.6.4-1 1-1h3.5c.6 0 1 .4 1 1 0 1.3.2 2.5.6 3.6.1.3 0 .7-.2 1z"/></svg>+61 0412 663 907</div>
    <div class="f-contact"><svg viewBox="0 0 24 24"><path d="M2 5h20v14H2zm2 2v.5l8 5 8-5V7zm0 2.8V17h16V9.8l-8 5z"/></svg>info@brelton.net.au</div>
  </div>
  <div class="abs f-col" style="left:643px;width:216px">
    <div class="f-head">Newsletter</div>
    <p class="f-text" style="margin-top:20px">Subpendisse tempus sodales neque,<br>eget eleifend turpis</p>
    <div class="f-input"></div>
    <div class="f-submit">Submit</div>
  </div>
  <div class="abs badge" role="img" aria-label="Industry association member badge"></div>
  <div class="abs diamonds"><span></span><span></span><span></span><span></span></div>
  <div class="abs copy"><span>Copyright © 2016 Brelton Engineering Pty Ltd All Rights Reserved EC 40317</span><span>Privacy Policy &nbsp;|&nbsp; Terms &amp; Condition</span></div>
</footer>

</body>
</html>
```